infographic

Infographic to be posted on chatterloop, website and shared by email very simply illustrating the below:

Meridian has doubled access to paid parental leave:
• Only about 50 per cent of working women had access to paid maternity leave before the Government introduced its scheme on 1 January 2011.
• Today 95 per cent of working women have access to paid parental leave (18 weeks at minimum wage)

Target Market(s)

women aged 30-45 with kids

Industry/Entity Type

Government

Requirements
Must have
• please use red for the 95% and blue for the 50% (red is meridian's colour)

```html
<!DOCTYPE html>
<html lang="en">
<head>
<meta charset="utf-8">
<title>Paid Parental Leave Infographic</title>
<link rel="stylesheet" href="https://fonts.googleapis.com/css2?family=PT+Sans:wght@400;700&family=Roboto+Condensed:wght@400;700&display=swap">
<style>
  :root {
    --bg-light: #f6f3ec;
    --bg-mid: #e2d9c8;
    --bg-edge: #c2b397;
    --grid: #555555;
    --axis: #777777;
    --label: #5e5e5e;
    --title: #333333;
    --blue-light: #2a78c8;
    --blue-mid: #1f4fa6;
    --blue-dark: #1a3584;
    --blue-top: #3f7fd0;
    --red-light: #ef4a38;
    --red-dark: #b8162a;
    --red-top: #f25a45;
    --value: #ffffff;
  }
  html, body {
    margin: 0;
    padding: 0;
    width: 1200px;
    height: 724px;
    overflow: hidden;
    background: var(--bg-edge);
  }
  .infographic {
    display: block;
    width: 1200px;
    height: 724px;
  }
  .axis-number {
    font-family: "PT Sans", sans-serif;
    font-size: 21px;
    fill: var(--label);
  }
  .axis-title-light {
    font-family: "PT Sans", sans-serif;
    font-size: 27px;
    fill: var(--title);
  }
  .axis-title-bold {
    font-family: "Roboto Condensed", sans-serif;
    font-weight: 700;
    font-size: 31px;
    fill: var(--title);
  }
  .bar-value {
    font-family: "PT Sans", sans-serif;
    font-weight: 700;
    font-size: 27px;
    fill: var(--value);
  }
  .timeline {
    font-family: "Roboto Condensed", sans-serif;
    fill: var(--title);
  }
  .timeline-small {
    font-size: 13px;
    font-weight: 400;
  }
  .timeline-date {
    font-size: 25px;
    font-weight: 700;
  }
  .sparkle { fill: #ffffff; }
</style>
</head>
<body>
<svg class="infographic" viewBox="0 0 1168 705" preserveAspectRatio="none" xmlns="http://www.w3.org/2000/svg" aria-label="Paid maternity leave access rose from 50% before 1 January 2011 to 95% after">
  <defs>
    <radialGradient id="backdrop" cx="470" cy="330" r="700" gradientUnits="userSpaceOnUse">
      <stop offset="0" stop-color="var(--bg-light)"/>
      <stop offset="0.45" stop-color="var(--bg-mid)"/>
      <stop offset="1" stop-color="var(--bg-edge)"/>
    </radialGradient>
    <linearGradient id="blue-left" x1="0" y1="0" x2="1" y2="0">
      <stop offset="0" stop-color="var(--blue-light)"/>
      <stop offset="1" stop-color="var(--blue-dark)"/>
    </linearGradient>
    <linearGradient id="blue-right" x1="0" y1="0" x2="1" y2="0">
      <stop offset="0" stop-color="var(--blue-light)"/>
      <stop offset="1" stop-color="var(--blue-mid)"/>
    </linearGradient>
    <linearGradient id="red-face" x1="0" y1="0" x2="1" y2="0">
      <stop offset="0" stop-color="var(--red-light)"/>
      <stop offset="1" stop-color="var(--red-dark)"/>
    </linearGradient>
  </defs>

  <rect class="backdrop" width="1168" height="705" fill="url(#backdrop)"/>

  <g class="gridlines" stroke="var(--grid)" fill="none">
    <line x1="315" y1="260" x2="925" y2="90" stroke-width="5" stroke-dasharray="22 11"/>
    <line x1="322" y1="336" x2="918" y2="158" stroke-width="4" stroke-dasharray="20 10"/>
    <line x1="330" y1="411" x2="912" y2="227" stroke-width="3.2" stroke-dasharray="18 9"/>
    <line x1="338" y1="485" x2="906" y2="292" stroke-width="2.4" stroke-dasharray="16 8"/>
    <line x1="346" y1="552" x2="902" y2="354" stroke-width="1.6" stroke-dasharray="14 7"/>
  </g>

  <g class="axes" stroke="var(--axis)" stroke-width="1.2" fill="none">
    <line x1="315" y1="260" x2="353" y2="615"/>
    <line x1="353" y1="615" x2="896" y2="410"/>
  </g>

  <g class="axis-numbers">
    <text class="axis-number" x="264" y="276">100</text>
    <text class="axis-number" x="283" y="350">80</text>
    <text class="axis-number" x="294" y="424">60</text>
    <text class="axis-number" x="304" y="497">40</text>
    <text class="axis-number" x="314" y="566">20</text>
    <text class="axis-number" x="333" y="631">0</text>
  </g>

  <g class="axis-title">
    <text class="axis-title-light" transform="translate(254 318) rotate(90)">% OF PAID</text>
    <text class="axis-title-bold" transform="translate(208 312) rotate(90)">MATERNITY LEAVE</text>
  </g>

  <g class="bar bar-before">
    <polygon points="363,348 432,425 440,585 375,508" fill="url(#blue-left)"/>
    <polygon points="432,425 518,395 524,552 440,585" fill="url(#blue-right)"/>
    <polygon points="363,348 452,322 518,395 432,425" fill="var(--blue-top)"/>
    <polyline points="363,348 432,425 518,395" fill="none" stroke="#ffffff" stroke-opacity="0.6" stroke-width="1"/>
    <line x1="432" y1="425" x2="440" y2="585" stroke="#ffffff" stroke-opacity="0.5" stroke-width="1"/>
    <path class="sparkle" d="M432 410 L435 422 L447 425 L435 428 L432 440 L429 428 L417 425 L429 422 Z"/>
    <text class="bar-value" x="450" y="491">50%</text>
  </g>

  <g class="bar bar-after">
    <polygon points="630,112 713,175 705,488 630,420" fill="url(#red-face)"/>
    <polygon points="713,175 790,150 778,462 705,488" fill="url(#red-face)"/>
    <polygon points="630,112 708,93 790,150 713,175" fill="var(--red-top)"/>
    <polyline points="630,112 713,175 790,150" fill="none" stroke="#ffffff" stroke-opacity="0.6" stroke-width="1"/>
    <line x1="713" y1="175" x2="705" y2="488" stroke="#ffffff" stroke-opacity="0.5" stroke-width="1"/>
    <path class="sparkle" d="M713 158 L716 172 L730 175 L716 178 L713 192 L710 178 L696 175 L710 172 Z"/>
    <path class="sparkle" d="M752 152 L754 158 L760 160 L754 162 L752 168 L750 162 L744 160 L750 158 Z"/>
    <text class="bar-value" x="720" y="256">95%</text>
  </g>

  <text class="timeline" transform="translate(482 608) rotate(-19.5)" textLength="328" lengthAdjust="spacingAndGlyphs"><tspan class="timeline-small">BEFORE </tspan><tspan class="timeline-date">← 1 January 2011 →</tspan><tspan class="timeline-small"> AFTER</tspan></text>
</svg>
</body>
</html>
```